Vantel company profile brochure

We are looking for a 2 - 4 page brochure for our company profile.
We’re Vantel, a team of town planning and traffic and transport engineering specialists located in Melbourne, Australia.
We would like a dynamic, exciting brochure that features the colours of our logo - blue, green and grey with orange as a feature colour.
The final result should convey that Vantel is:
-Reassuring and trustworthy
-Honest and direct
- Friendly and a bit kooky
-Laid-back and casual
-Fun to work with
-Highly knowledgeable within specific areas of expertise
-Polished and professional but not afraid to show a bit of personality
-Not as ‘hard edge’ as other planners or engineers
Vantel Consultants have created a business based on providing niche, expert advice across the two main areas of urban planning and traffic engineering as well as growing areas such as social and economic analysis. They are fiercely proud of the things that make them different to other firms – they take their responsibilities seriously, they are honest and up-front, they know how to work hard but also how to relax and have a laugh, and perhaps most importantly they know how to relate to people and they care about building successful relationships with their clients, colleagues and their staff. Vantel Consultants are united by our passion for shaping the city and their desire to ensure it develops sustainably.
Many similar businesses share some of these qualities, but Vantel is rare in that they deliver the whole package. This is evidenced by our ability to attract and retain high quality staff, by our long-standing client relationships and by their commitment to progressing our own company by commissioning a brochure and business card.

Target Market(s)

Vantel’s diverse client base consists of architecture practices, builders and developers, local government and the legal fraternity so these are the areas we market to.

Industry/Entity Type

Building

Requirements
Must have
• Must use our logos colours and logo.
The logo can be altered in that the type and image do not have stay exactly as it is on the JPEG - the words and image can be placed apart / together etc.
Nice to have
• We would like an image on the front cover that we can change
Page about disciplines

```html
<!DOCTYPE html>
<html lang="en">
<head>
<meta charset="utf-8">
<title>Vantel Disciplines Spread</title>
<link href="https://fonts.googleapis.com/css2?family=Source+Sans+3:wght@300;400;700&display=swap" rel="stylesheet">
<style>
  :root{
    --backdrop:#2b2b2c;
    --paper:#e4e5e6;
    --band:#a6a9ac;
    --band-dark:#7d8083;
    --blue:#1a6fc0;
    --green:#3aaa4a;
    --green-soft:rgba(58,170,74,.82);
    --orange:#f08a1d;
    --ink:#1f2226;
    --white:#ffffff;
    --logo-grey:#6c7177;
  }
  *{margin:0;padding:0;box-sizing:border-box}
  html,body{width:1200px;height:793px;overflow:hidden;background:var(--backdrop)}
  body{font-family:"Source Sans 3",Arial,sans-serif;color:var(--ink)}
  .spread{position:absolute;left:140px;top:72px;width:925px;height:650px;background:var(--paper);overflow:hidden}
  .abs{position:absolute}
  .photo-planner{left:0;top:0;width:460px;height:506px;
    background:linear-gradient(100deg,#f2f2f2 0%,#dcdcdc 35%,#b7b7b7 52%,#d8d8d8 70%,#eeeeee 100%)}
  .panel-right-top{left:460px;top:0;width:465px;height:225px;background:linear-gradient(#e8e9ea,#d7d9db)}
  .photo-traffic{left:460px;top:225px;width:465px;height:101px;
    background:linear-gradient(90deg,#2a3f5c 0%,#4b6a8c 30%,#c9743e 55%,#e6a05c 62%,#3b5577 80%,#22344e 100%)}
  .panel-right-mid{left:460px;top:326px;width:465px;height:180px;background:linear-gradient(#d6d8da,#c3c5c8)}
  .band{left:0;top:506px;width:925px;height:144px;background:var(--band);border-top:3px solid #f4f4f4}
  .band-foot{left:0;top:633px;width:925px;height:17px;background:var(--band-dark)}
  .fold{left:459px;top:0;width:2px;height:650px;background:linear-gradient(90deg,rgba(0,0,0,.08),rgba(255,255,255,.12))}

  .title{color:var(--white);font-weight:300;line-height:1;letter-spacing:-.5px}
  .tab-blue{left:20px;top:25px;width:178px;height:55px;background:var(--blue);
    clip-path:polygon(0 0,158px 0,158px 22px,178px 32px,158px 42px,158px 100%,0 100%)}
  .tab-blue .title{font-size:41px;position:absolute;left:8px;top:7px}
  .box-blue{left:20px;top:80px;width:158px;height:73px;background:var(--blue)}
  .panel-white{left:20px;top:153px;width:160px;height:284px;background:rgba(255,255,255,.88)}

  .tab-green{left:380px;top:15px;width:177px;height:55px;background:var(--green);
    clip-path:polygon(0 0,150px 0,150px 18px,177px 28px,150px 38px,150px 100%,0 100%)}
  .tab-green .title{font-size:40px;position:absolute;left:4px;top:6px}
  .box-green{left:380px;top:70px;width:150px;height:98px;background:var(--green-soft)}
  .tab-green.lower{top:326px;height:56px}
  .box-green.lower{top:382px;height:96px}

  .tab-orange{left:20px;top:515px;width:140px;height:62px;background:var(--orange);
    clip-path:polygon(0 0,128px 0,128px 19px,140px 27px,128px 35px,128px 100%,0 100%)}
  .tab-orange .title{font-size:27px;position:absolute;left:5px;top:5px;line-height:.95}
  .tab-orange.alt{left:380px;width:132px;clip-path:polygon(0 0,120px 0,120px 19px,132px 27px,120px 35px,120px 100%,0 100%)}
  .tab-orange.alt .title{font-size:29px;top:14px}

  .copy{font-size:7.2px;line-height:9px}
  .copy h4{font-size:7.6px;font-weight:700;margin:2px 0 7px}
  .copy p{margin-bottom:7px}
  .service{font-size:6.9px;line-height:8.3px}
  .service h3{font-size:8.8px;font-weight:700;line-height:9.6px}
  .col-a{left:568px;width:170px}
  .col-b{left:748px;width:168px}
  .on-colour{color:var(--white)}
  .on-band{color:#f3f3f3}

  .brand{left:718px;top:588px;display:flex;align-items:center;gap:8px}
  .brand-square{width:14px;height:14px;background:var(--blue)}
  .brand-name{font-size:42px;font-weight:400;color:var(--logo-grey);letter-spacing:1px;line-height:1}
</style>
</head>
<body>
<div class="spread">
  <div class="abs photo-planner" role="img" aria-label="Photo of a planner in a hard hat and shirt standing before sketched city drawings"></div>
  <div class="abs panel-right-top"></div>
  <div class="abs photo-traffic" role="img" aria-label="Motion-blurred photo of traffic on a city road at dusk"></div>
  <div class="abs panel-right-mid"></div>
  <div class="abs band"></div>
  <div class="abs band-foot"></div>
  <div class="abs fold"></div>

  <!-- Planning -->
  <div class="abs tab-blue"><h2 class="title">Planning</h2></div>
  <div class="abs box-blue"></div>
  <p class="abs copy on-colour" style="left:30px;top:86px;width:140px">We use our extensive knowledge and experience to help our clients successfully navigate each step of the statutory and strategic planning processes.</p>
  <div class="abs panel-white"></div>
  <div class="abs copy" style="left:30px;top:161px;width:142px">
    <h4>Permit Applications</h4>
    <p>We have obtained planning permits for our clients on a variety of residential, commercial, entertainment and industrial projects in Melbourne, regional Victoria and interstate. Our consultative approach and extensive experience allows us to identify and resolve potential issues quickly.</p>
    <h4>CPAT Advocacy</h4>
    <p>Due to our industry expertise, Vantel’s planning team are regularly appointed as CPAT advocates for private and public clients. We have acted as representatives for diverse project types at CPAT appeals, mediations, planning panels and Consumer Standards Office appeals.</p>
    <h4>CPAT Expert Evidence</h4>
    <p>XXXX [hyperlink to bio’s] frequently present expert evidence before CPAT and planning panels for a range of urban planning projects. They work closely with members of the legal fraternity, private and public clients to facilitate positive outcomes by applying their specialist knowledge.</p>
  </div>

  <!-- Traffic -->
  <div class="abs tab-green"><h2 class="title">Traffic</h2></div>
  <div class="abs box-green"></div>
  <p class="abs copy on-colour" style="left:384px;top:86px;width:142px">Vantel’s traffic engineering experts assess, analyse and design road systems and traffic management plans, working closely with our planning and transport teams.</p>

  <div class="abs service col-a" style="top:23px">
    <h3>Traffic Impact Assessment</h3>
    <p>Our team’s knowledge and experience gives us the ability to efficiently and accurately develop Traffic Impact Reports to accompany planning applications. We work across residential, commercial, industrial, sports and institutional projects and have worked with private developers and local government.</p>
  </div>
  <div class="abs service col-a" style="top:93px">
    <h3>CPAT Expert Evidence</h3>
    <p>XXXX [hyperlink to bio’s] frequently present expert evidence before CPAT and planning panels for a range of traffic projects. They assist members of the legal fraternity, private and public clients to facilitate positive outcomes by applying their specialist knowledge.</p>
  </div>
  <div class="abs service col-a" style="top:154px">
    <h3>Traffic System Design</h3>
    <p>We design and plan traffic facilities for private developers and government including the detailed design of traffic signal systems for urban arterial intersections. Our experience covers both the development of new systems and the design of upgrades to existing traffic system facilities.</p>
  </div>
  <div class="abs service col-b" style="top:23px">
    <h3>Local Area Traffic Management</h3>
    <p>Vantel collaborates with local governments to develop traffic management plans that address traffic, safety and amenity issues for residential areas. We have worked on projects that feature highly sensitive, complex land uses such as schools, childcare centres and kindergartens.</p>
  </div>
  <div class="abs service col-b" style="top:93px">
    <h3>Road Safety Audits</h3>
    <p>We plan and assess road safety for a range of private and public sector clients. Our extensive experience includes Municipal Road Safety Strategies for over 20 Victorian local councils as well as road safety audits for road works and proposed development sites.</p>
  </div>
  <div class="abs service col-b" style="top:154px">
    <h3>Car Parking</h3>
    <p>Vantel works with private and public clients, as well as architects and civil engineers, to prepare precinct parking plans, assess parking uses for new developments as well as assist with the planning and design of at-grade and multi-storey car parks.</p>
  </div>

  <!-- Transport -->
  <div class="abs tab-green lower"><h2 class="title">Transport</h2></div>
  <div class="abs box-green lower"></div>
  <p class="abs copy on-colour" style="left:384px;top:410px;width:142px">Vantel’s transport planning team offers our clients high level, accurate, strategic advice, which prioritises sustainable transport including walking, cycling and public transport.</p>

  <div class="abs service col-a" style="top:339px">
    <h3>Sustainable Transport Planning</h3>
    <p>From public transport to bike-sharing, Vantel works with private and public clients to research, plan and recommend the most suitable sustainable transport solutions for the specific needs of each project. Where needed, our team seamlessly integrates with Vantel’s planning and traffic engineering teams.</p>
  </div>
  <div class="abs service col-a" style="top:417px">
    <h3>Green Travel Plans</h3>
    <p>Green travel is an increasing priority in today’s world – we work with multiple stakeholders to determine the best methods to promote and achieve sustainable transport options such as walking, cycling, car-sharing and public transport for a range of organisations including schools, workplaces and new development sites.</p>
  </div>
  <div class="abs service col-b" style="top:339px">
    <h3>Major Event Planning</h3>
    <p>Vantel works with major sports and entertainment event organisers to create safe and secure traffic plans that protect competitors, participants and spectators. We recognise the unique transport requirements of large-scale events and the difference that good planning makes.</p>
  </div>
  <div class="abs service col-b" style="top:409px">
    <h3>Bike Planning</h3>
    <p>Melbourne is known as a “cycle city” and Vantel’s transport team designs and assesses bicycle and pedestrian facilities, often as a component of larger road safety projects. We have experience with DDA compliance and our projects consider the special needs of pedestrians.</p>
  </div>

  <!-- Social & Economic -->
  <div class="abs tab-orange"><h2 class="title">Social &amp;<br>Economic</h2></div>
  <p class="abs service on-band" style="left:24px;top:580px;width:140px">Vantel offers the unique combination of social and economic planning services. Our team’s expertise covers social impact assessments, demographic analysis and community attitude surveys.</p>
  <div class="abs service on-band" style="left:181px;top:516px;width:192px">
    <h3>Social and Economic Impact Statement</h3>
    <p>Vantel has an excellent reputation for delivering social and economic impact statements, including for the gaming industry. These projects combine our high level of sensitivity to complex community issues with our expertise in strategic demographic analysis.</p>
  </div>
  <div class="abs service on-band" style="left:181px;top:578px;width:192px">
    <h3>Liquor Licensing</h3>
    <p>We have extensive experience assessing the impact of bars and clubs on local communities through consultation and analysis. Members of our team have also appeared before CPAT and Consumer Standards Office representing our clients on a range of liquor related matters.</p>
  </div>

  <!-- Additional -->
  <div class="abs tab-orange alt"><h2 class="title">Additional</h2></div>
  <p class="abs service on-band" style="left:384px;top:580px;width:136px">Vantel offers some additional planning-related services. We have considerable experience in Due Diligence and Property Advice projects for a range of clients.</p>
  <div class="abs service on-band" style="left:541px;top:516px;width:168px">
    <h3>Due Diligence</h3>
    <p>We perform thorough research and analysis on potential properties in order to determine their accurate value for our clients, mitigating the risk of significant property transactions.</p>
  </div>
  <div class="abs service on-band" style="left:541px;top:569px;width:168px">
    <h3>Property Advice</h3>
    <p>We use our urban planning and land use expertise to analyse the development potential of specific properties, advising our clients as to whether the land will be suitable for their needs and objectives.</p>
  </div>

  <div class="abs brand">
    <span class="brand-square"></span>
    <span class="brand-name">vantel</span>
  </div>
</div>
</body>
</html>
```